BOLD & MINIMALIST DESIGN NEEDED

We want a very bold but minimalistic business card design that is impactful and utilizes both sides of the business card. Our current logo is included for your use.

We want bold fonts and good use of negative space. We don't want the logo to overpower the design.

Target Market(s)

Professionals who are building new commercial buildings.

Industry/Entity Type

Construction

Contact Information for Business Card

Name, Title, email, office phone, cell phone, website

Font styles to use
Serif
Sans Serif

Requirements
Must have
• Bold design!

```html
<!DOCTYPE html>
<html lang="en">
<head>
<meta charset="utf-8">
<title>Ridgeline Design + Build — Business Card</title>
<link rel="stylesheet" href="https://fonts.googleapis.com/css2?family=Montserrat:wght@400;500;700;800&display=swap">
<style>
  :root {
    --stage: #3a3a3a;
    --green: #8cc63f;
    --green-light: #a9d86a;
    --green-deep: #3f7a2e;
    --ink: #0e0f10;
    --paper: #ffffff;
    --white-text: #f2f2f2;
  }
  * { margin: 0; padding: 0; box-sizing: border-box; }
  html, body {
    width: 1200px; height: 689px; overflow: hidden;
    background: var(--stage);
    font-family: "Montserrat", sans-serif;
  }
  .canvas { position: relative; width: 1200px; height: 689px; }
  .card {
    position: absolute; top: 190px;
    width: 540px; height: 309px;
    border-radius: 22px; overflow: hidden;
    box-shadow: 0 18px 40px rgba(0,0,0,.45);
  }
  /* Front */
  .card-front {
    left: 50px;
    background: linear-gradient(120deg, var(--green-light) 0%, var(--green) 45%, var(--green) 100%);
    display: flex; align-items: center; justify-content: center;
  }
  .front-wordmark {
    font-weight: 800; font-size: 52px; letter-spacing: 1px;
    color: var(--green-deep); display: flex; align-items: center; gap: 14px;
  }
  .front-wordmark .mark-square { width: 22px; height: 22px; background: var(--green-deep); }
  /* Back */
  .card-back { left: 630px; background: var(--paper); }
  .card-back .wave { position: absolute; inset: 0; }
  .back-wordmark {
    position: absolute; top: 32px; right: 70px;
    font-weight: 800; font-size: 30px; color: var(--ink);
  }
  .address {
    position: absolute; right: 24px; top: 150px; text-align: right;
    color: var(--white-text); font-size: 12px; line-height: 1.5;
  }
  .person { position: absolute; left: 30px; top: 170px; }
  .person-name { color: var(--green); font-weight: 800; font-size: 22px; letter-spacing: .5px; }
  .person-title { color: var(--white-text); font-size: 11px; font-weight: 500; letter-spacing: .5px; margin-top: 1px; }
  .contact-list { list-style: none; margin-top: 9px; }
  .contact-list li {
    display: flex; align-items: center; gap: 8px;
    color: var(--white-text); font-size: 11.5px; line-height: 17px;
  }
  .contact-list svg { width: 11px; height: 11px; fill: var(--green); flex: none; }
</style>
</head>
<body>
<main class="canvas">

  <section class="card card-front" aria-label="Card front">
    <div class="front-wordmark"><span class="mark-square"></span>RIDGELINE</div>
  </section>

  <section class="card card-back" aria-label="Card back">
    <svg class="wave" viewBox="0 0 540 309" preserveAspectRatio="none" aria-hidden="true">
      <path d="M0,150 C60,128 150,112 270,108 C400,102 490,78 540,30" fill="none" stroke="var(--ink)" stroke-width="5"/>
      <path d="M0,168 C60,146 150,134 270,128 C400,121 490,96 540,48" fill="none" stroke="var(--green)" stroke-width="6"/>
      <path d="M0,176 C60,154 150,142 270,136 C400,129 490,104 540,56 L540,309 L0,309 Z" fill="var(--ink)"/>
    </svg>

    <div class="back-wordmark">RIDGELINE</div>

    <p class="address">Your address, City<br>State, Zip 1234</p>

    <div class="person">
      <h1 class="person-name">MARCUS VALE</h1>
      <p class="person-title">OWNER-CEO</p>
      <ul class="contact-list">
        <li><svg viewBox="0 0 12 12"><path d="M2 1h3l1 3-1.5 1a6 6 0 0 0 2.5 2.5L8 6l3 1v3a1 1 0 0 1-1 1A9 9 0 0 1 1 2a1 1 0 0 1 1-1z"/></svg>123 456 789</li>
        <li><svg viewBox="0 0 12 12"><path d="M3 0h6a1 1 0 0 1 1 1v10a1 1 0 0 1-1 1H3a1 1 0 0 1-1-1V1a1 1 0 0 1 1-1zm0 2v7h6V2z"/></svg>123 456 789</li>
        <li><svg viewBox="0 0 12 12"><path d="M0 2h12v8H0zm1 1v.5l5 3.5 5-3.5V3z"/></svg>info@youremail.com</li>
        <li><svg viewBox="0 0 12 12"><circle cx="6" cy="6" r="5.5"/></svg>www.yourwebsite.com</li>
      </ul>
    </div>
  </section>

</main>
</body>
</html>
```